Lurna Beauty Mobile App Design

We need an app design for a new on-demand beauty service app called Lurna Beauty. We help customers find and book beauty services on-demand (within 48 hours) or into the future. We would like to see designs that are clean and include the logs colors with dark and light shades of grey.
Design should be clean and modern yet showcase that this is a beauty app. It should beautiful and artful as well.
One set of mockups are attached, another set exists.
Competitors include primwick.example or dovatrine.example
Key: You can change the mockups to be best suited for functionality and design. These are here for content only.
Updates
The designs so far look great! Can you please design the portfolio screen for me to see navigation and a registration page to see your idea of textbox and buttons.
Industry/Entity Type
It Service
Look and feel
Each slider illustrates characteristics of the customer's brand and the style your logo design should communicate.

```html
<!DOCTYPE html>
<html lang="en">
<head>
<meta charset="utf-8">
<title>Lurna Beauty – App Screens</title>
<link rel="stylesheet" href="https://fonts.googleapis.com/css2?family=Open+Sans:wght@300;400;600&display=swap">
<style>
  :root{
    --canvas:#f0f0f0;
    --plum:#a8318f;
    --rose:#f0709b;
    --brand-ink:#6b1f5c;
    --ink:#1b1b1b;
    --mint:#80d57e;
    --mint-dim:#5f9c60;
    --field:#ffffff;
    --field-muted:#c4c4c4;
    --panel:#e4e4e4;
    --alert-blue:#2f8cf0;
    --white:#ffffff;
  }
  *{box-sizing:border-box;margin:0;padding:0}
  html,body{width:1200px;height:1000px;overflow:hidden;background:var(--canvas)}
  body{position:relative;font-family:"Open Sans",sans-serif;font-weight:300;color:var(--ink)}

  .screen{position:absolute;overflow:hidden;
    background:linear-gradient(170deg,var(--plum) 0%,#c9458f 45%,var(--rose) 100%)}
  .abs{position:absolute}
  .center{left:0;right:0;text-align:center}

  .status{position:absolute;top:4px;left:6px;right:6px;display:flex;justify-content:space-between;
    font-size:5px;font-weight:400;color:var(--ink)}
  .status--large{top:9px;left:10px;right:8px;font-size:12px;color:var(--white)}

  .brand-name{font-size:15px;letter-spacing:1px;color:var(--brand-ink);font-weight:400}
  .brand-tag{font-size:4.5px;color:var(--brand-ink);font-weight:400}

  .steps{font-size:8px;line-height:15px;color:var(--ink)}
  .body-copy{font-size:7.5px;line-height:10px;color:var(--ink);padding:0 10px}
  .dots{display:flex;justify-content:center;gap:4px}
  .dots span{width:3px;height:3px;border-radius:50%;background:#9b5e86}
  .dots span.on{background:var(--ink)}

  .pill{position:absolute;border-radius:14px;display:flex;align-items:center;justify-content:center;
    font-size:7px;color:var(--ink);font-weight:400}
  .pill--mint{background:var(--mint)}
  .pill--dark{background:var(--ink);color:var(--white)}
  .field{position:absolute;background:var(--field);border-radius:14px;display:flex;align-items:center;
    gap:3px;padding-left:12px;font-size:5.5px;color:var(--ink);font-weight:400}
  .field svg{width:6px;height:6px}
  .field--muted{background:var(--field-muted);font-size:9px;padding-left:20px;border-radius:18px;gap:5px}
  .field--muted svg{width:9px;height:9px}

  .nav-title{font-size:11px;color:var(--white);font-weight:400}
  .back{position:absolute;width:7px;height:7px}
  .link{font-size:6px;color:var(--white);font-weight:400}
  .terms{font-size:6px;line-height:8px;color:var(--ink);font-weight:400}

  /* menu screen */
  .menu-title{font-size:26px;color:var(--white)}
  .side-panel{position:absolute;left:327px;top:65px;width:50px;bottom:0;background:var(--panel)}
  .avatar{position:absolute;left:42px;top:115px;width:171px;height:171px;border-radius:50%;
    background:radial-gradient(circle at 45% 40%,#b98a72 0%,#6b4a3a 55%,#3f4a34 100%)}
  .profile-name{position:absolute;left:0;width:266px;top:290px;text-align:center;font-size:26px;color:var(--white)}
  .menu-item{position:absolute;left:56px;display:flex;align-items:center;gap:18px;font-size:20px;color:var(--white)}
  .menu-item svg{width:24px;height:24px}

  /* dimmed sign-up */
  .dim{position:absolute;inset:0;background:rgba(40,10,40,.28)}
  .alert{position:absolute;left:36px;top:136px;width:170px;height:64px;background:var(--white);
    text-align:center;font-size:10px;font-weight:400}
  .alert p{padding-top:14px}
  .alert hr{border:0;border-top:1px solid #ddd;margin:6px 0 0}
  .alert .ok{color:var(--alert-blue);font-weight:600;padding-top:5px}
</style>
</head>
<body>

<!-- Splash -->
<section class="screen" style="left:62px;top:110px;width:164px;height:295px">
  <div class="status"><span>●●●●○ NOVA</span><span>4:21 PM</span><span>100%</span></div>
  <div class="abs center brand-name" style="top:73px">LURNA BEAUTY</div>
  <div class="abs center brand-tag" style="top:92px">On-Demand Beauty Services</div>
  <div class="abs center steps" style="top:120px">1. Pick your look<br>2. Select your date and time<br>3. Pick your artist<br>4. Ready to go</div>
  <div class="abs center dots" style="top:192px"><span class="on"></span><span></span><span></span><span></span></div>
  <div class="pill pill--mint" style="left:20px;top:207px;width:124px;height:24px">LOGIN</div>
  <div class="pill pill--dark" style="left:20px;top:237px;width:124px;height:24px">SIGN UP</div>
  <div class="abs center link" style="top:278px">Artist : Sign up here &gt;&gt;</div>
</section>

<!-- Intro slide -->
<section class="screen" style="left:355px;top:110px;width:166px;height:295px">
  <div class="status"><span>●●●●○ NOVA</span><span>4:21 PM</span><span>100%</span></div>
  <div class="abs center" style="top:58px;font-size:18px;font-weight:400">HEADER</div>
  <div class="abs center brand-tag" style="top:79px;color:var(--ink)">Sub header</div>
  <div class="abs center body-copy" style="top:102px">Lorem ipsum dolor sit amet, consectetur adipiscing elit. Nullam in rutrum nibh. Ut tincidunt diam odio, a elementum velit scelerisque at. Donec eget magna et metus hendrerit luctus. Praesent interdum ipsum lacus, sed accumsan odio eleifend accumsan.</div>
  <div class="abs center dots" style="top:196px"><span></span><span class="on"></span><span></span><span></span></div>
  <div class="pill pill--mint" style="left:20px;top:210px;width:126px;height:24px">LOGIN</div>
  <div class="pill pill--dark" style="left:20px;top:241px;width:126px;height:24px">SIGN UP</div>
  <div class="abs center link" style="top:282px">Artist : Sign up here &gt;&gt;</div>
</section>

<!-- Log in -->
<section class="screen" style="left:70px;top:607px;width:166px;height:296px">
  <div class="status"><span>●●●●○ NOVA</span><span>4:21 PM</span><span>100%</span></div>
  <svg class="back" style="left:9px;top:21px" viewBox="0 0 8 8"><path d="M5.5 1 2.5 4l3 3" fill="none" stroke="#fff" stroke-width="1.4"/></svg>
  <div class="abs center nav-title" style="top:17px">Log in</div>
  <div class="abs center brand-name" style="top:85px">LURNA BEAUTY</div>
  <div class="abs center brand-tag" style="top:104px">On-Demand Beauty Services</div>
  <div class="field" style="left:22px;top:137px;width:125px;height:25px">
    <svg viewBox="0 0 6 6"><circle cx="3" cy="1.8" r="1.4" fill="#1b1b1b"/><path d="M0.5 6a2.5 2.3 0 0 1 5 0z" fill="#1b1b1b"/></svg>E-mail</div>
  <div class="field" style="left:22px;top:172px;width:125px;height:25px">
    <svg viewBox="0 0 6 6"><rect x="1" y="2.6" width="4" height="3.2" fill="#1b1b1b"/><path d="M1.8 2.8V1.9a1.2 1.2 0 0 1 2.4 0v.9" fill="none" stroke="#1b1b1b" stroke-width=".7"/></svg>Password</div>
  <div class="pill pill--mint" style="left:20px;top:209px;width:125px;height:24px">LOGIN</div>
  <div class="abs center" style="top:237px;font-size:5.5px;font-weight:400">Forgot Password?</div>
</section>

<!-- Sign up -->
<section class="screen" style="left:362px;top:602px;width:167px;height:295px">
  <div class="status"><span>●●●●○ NOVA</span><span>4:21 PM</span><span>100%</span></div>
  <svg class="back" style="left:10px;top:21px" viewBox="0 0 8 8"><path d="M5.5 1 2.5 4l3 3" fill="none" stroke="#fff" stroke-width="1.4"/></svg>
  <div class="abs center nav-title" style="top:17px">Sign up</div>
  <div class="field" style="left:24px;top:45px;width:128px;height:24px">First Name</div>
  <div class="field" style="left:24px;top:79px;width:128px;height:24px">Last Name</div>
  <div class="field" style="left:24px;top:111px;width:128px;height:24px">
    <svg viewBox="0 0 6 6"><circle cx="3" cy="1.8" r="1.4" fill="#1b1b1b"/><path d="M0.5 6a2.5 2.3 0 0 1 5 0z" fill="#1b1b1b"/></svg>E-mail</div>
  <div class="field" style="left:24px;top:145px;width:128px;height:24px">
    <svg viewBox="0 0 6 6"><rect x="1" y="2.6" width="4" height="3.2" fill="#1b1b1b"/><path d="M1.8 2.8V1.9a1.2 1.2 0 0 1 2.4 0v.9" fill="none" stroke="#1b1b1b" stroke-width=".7"/></svg>Password</div>
  <div class="field" style="left:24px;top:179px;width:128px;height:24px">
    <svg viewBox="0 0 6 6"><rect x=".5" y=".5" width="2" height="2" fill="#1b1b1b"/><rect x="3.5" y=".5" width="2" height="2" fill="#1b1b1b"/><rect x=".5" y="3.5" width="2" height="2" fill="#1b1b1b"/><rect x="3.5" y="3.5" width="2" height="2" fill="#1b1b1b"/></svg>Enter referrer code :</div>
  <div class="abs center terms" style="top:218px">By clicking below you agree to the<br>terms and conditions of Lurna.</div>
  <div class="pill pill--mint" style="left:24px;top:251px;width:128px;height:24px">Create Account</div>
</section>

<!-- Navigation menu -->
<section class="screen" style="left:603px;top:168px;width:377px;height:672px">
  <div class="status status--large"><span>●●●○○ NOVA</span><span>4:21 PM</span><span>100%</span></div>
  <svg class="abs" style="left:22px;top:46px;width:26px;height:20px" viewBox="0 0 26 20">
    <g fill="#fff"><rect x="0" y="2" width="3" height="3"/><rect x="6" y="2.5" width="20" height="2"/><rect x="0" y="9" width="3" height="3"/><rect x="6" y="9.5" width="20" height="2"/><rect x="0" y="16" width="3" height="3"/><rect x="6" y="16.5" width="20" height="2"/></g></svg>
  <div class="abs center menu-title" style="top:37px">Lurna</div>
  <div class="side-panel"></div>
  <div class="avatar" role="img" aria-label="Profile photo of the signed-in customer"></div>
  <div class="profile-name">Mira Coldwell</div>

  <div class="menu-item" style="top:366px">
    <svg viewBox="0 0 24 24"><path d="M12 2l2.9 6.9 7.1.6-5.4 4.7 1.7 7.3L12 17.6 5.7 21.5l1.7-7.3L2 9.5l7.1-.6z" fill="#fff"/></svg>New Service</div>
  <div class="menu-item" style="top:424px">
    <svg viewBox="0 0 24 24"><circle cx="12" cy="12" r="8" fill="none" stroke="#fff" stroke-width="4" stroke-dasharray="3.1 3.2"/><circle cx="12" cy="12" r="6.5" fill="#fff"/><circle cx="12" cy="12" r="3" fill="#c9458f"/></svg>Settings</div>
  <div class="menu-item" style="top:486px">
    <svg viewBox="0 0 24 24"><g fill="none" stroke="#fff" stroke-width="2.4"><circle cx="6" cy="6" r="3"/><circle cx="18" cy="6" r="3"/><path d="M6 9v13M18 9v13M3 19l3 3 3-3M15 19l3 3 3-3"/></g></svg>Share</div>
  <div class="menu-item" style="top:542px">
    <svg viewBox="0 0 24 24"><g fill="none" stroke="#fff" stroke-width="2"><path d="M5 2h12v20H5z"/></g><path d="M5 2l8 3v17l-8-0z" fill="#fff"/><path d="M18 12h5M21 10l2 2-2 2" stroke="#fff" stroke-width="1.6" fill="none"/></svg>Logout</div>
</section>

<!-- Sign up with referrer alert -->
<section class="screen" style="left:927px;top:462px;width:234px;height:422px">
  <div class="status" style="font-size:6px"><span>●●●●○ NOVA</span><span>4:21 PM</span><span>100%</span></div>
  <svg class="back" style="left:12px;top:30px;width:10px;height:10px" viewBox="0 0 8 8"><path d="M5.5 1 2.5 4l3 3" fill="none" stroke="#fff" stroke-width="1.4"/></svg>
  <div class="abs center nav-title" style="top:25px;font-size:16px">Sign up</div>
  <div class="field field--muted" style="left:31px;top:61px;width:179px;height:36px">First Name</div>
  <div class="field field--muted" style="left:31px;top:109px;width:179px;height:36px">Last Name</div>
  <div class="field field--muted" style="left:31px;top:157px;width:179px;height:36px">E-mail</div>
  <div class="field field--muted" style="left:31px;top:203px;width:179px;height:36px">
    <svg viewBox="0 0 6 6"><rect x="1" y="2.6" width="4" height="3.2" fill="#1b1b1b"/><path d="M1.8 2.8V1.9a1.2 1.2 0 0 1 2.4 0v.9" fill="none" stroke="#1b1b1b" stroke-width=".7"/></svg>Password</div>
  <div class="field field--muted" style="left:31px;top:249px;width:179px;height:36px">
    <svg viewBox="0 0 6 6"><rect x=".5" y=".5" width="2" height="2" fill="#1b1b1b"/><rect x="3.5" y=".5" width="2" height="2" fill="#1b1b1b"/><rect x=".5" y="3.5" width="2" height="2" fill="#1b1b1b"/><rect x="3.5" y="3.5" width="2" height="2" fill="#1b1b1b"/></svg>Enter referrer code :</div>
  <div class="abs center terms" style="top:304px;font-size:8.5px;line-height:12px">By clicking below you agree to the<br>terms and conditions of Lurna.</div>
  <div class="pill pill--mint" style="left:31px;top:350px;width:179px;height:35px;font-size:11px;color:#eee">Create Account</div>
  <div class="dim"></div>
  <div class="alert"><p>Referrer code not found.</p><hr><div class="ok">OK</div></div>
</section>

</body>
</html>
```